MEKO Business Card Design

I have a rough idea of the design / layout of the company business card but need help in finalizing the design and quality.

I'm looking for the card to be stand out, but simple, on the front with clear detail on the back with space for some one to write any other detail they need onto the card. The rough draft includes the crinkled graph paper back ground which I quite like for the front.

I will need the card design completed and ready to print in Australian business card standard sizes. This includes detail on all colors, fonts and type faces used as well as copy of the original for editing (inserting other employee details).

I have included the company logo and a rough draft of the card, including the graphic I would like to use for the back ground on the front, I am not sure that the graphic is any good for printing, not the highest res.

Thanks,

Lyle

```html
<!DOCTYPE html>
<html lang="en">
<head>
<meta charset="utf-8">
<title>MEKO Business Card – Lyle Hartwell</title>
<link rel="stylesheet" href="https://fonts.googleapis.com/css2?family=Arimo:wght@700&family=Crimson+Text&family=Dancing+Script:wght@500&display=swap">
<style>
  :root {
    --paper: #ffffff;
    --ink: #111111;
    --brand: #1c1c1c;
    --rule: #222222;
  }
  html, body {
    margin: 0;
    padding: 0;
    width: 1200px;
    height: 733px;
    overflow: hidden;
    background: var(--paper);
  }
  .card {
    position: relative;
    width: 1200px;
    height: 733px;
    background: var(--paper);
    color: var(--ink);
  }
  .brand-name {
    position: absolute;
    left: 88px;
    top: 52px;
    margin: 0;
    font-family: "Arimo", Arial, sans-serif;
    font-weight: 700;
    font-size: 82px;
    line-height: 1;
    letter-spacing: -2px;
    color: var(--brand);
  }
  .person {
    position: absolute;
    left: 71px;
    top: 310px;
    width: 358px;
  }
  .person-name {
    margin: 0;
    padding: 0 0 6px 8px;
    font-family: "Arimo", Arial, sans-serif;
    font-weight: 700;
    font-size: 42px;
    line-height: 1.1;
    color: var(--ink);
    border-bottom: 2px solid var(--rule);
  }
  .person-role {
    margin: 2px 0 0 4px;
    font-family: "Dancing Script", cursive;
    font-weight: 500;
    font-size: 40px;
    line-height: 1.1;
    color: var(--ink);
  }
  .contact-list {
    position: absolute;
    left: 592px;
    top: 366px;
    margin: 0;
    padding: 0;
    list-style: none;
    font-family: "Crimson Text", Georgia, serif;
    font-size: 35px;
    line-height: 47.5px;
    color: var(--ink);
  }
  .contact-item {
    display: flex;
    align-items: center;
    white-space: nowrap;
  }
  .contact-icon {
    width: 28px;
    height: 28px;
    margin-right: 10px;
    flex: none;
    fill: none;
    stroke: var(--ink);
    stroke-width: 2.4;
  }
  .contact-icon .solid { fill: var(--ink); stroke: none; }
  .contact-indent { padding-left: 38px; }
</style>
</head>
<body>
<main class="card">
  <h1 class="brand-name">MEKO</h1>

  <section class="person">
    <h2 class="person-name">LYLEHARTWELL</h2>
    <p class="person-role">Operations Manager</p>
  </section>

  <ul class="contact-list">
    <li class="contact-item">
      <svg class="contact-icon" viewBox="0 0 28 28" aria-hidden="true">
        <rect x="3" y="8" width="22" height="15"/>
        <path d="M3 8 L14 17 L25 8"/>
      </svg>
      lhartwell@meko.com.au
    </li>
    <li class="contact-item">
      <svg class="contact-icon" viewBox="0 0 28 28" aria-hidden="true">
        <path class="solid" d="M7 5 L11 5 L13 10 L10.5 12 C12 15.5 13.5 17 16.5 18.5 L18.5 16 L23.5 18 L23.5 22 C23.5 23.5 22 24.5 20.5 24.3 C12 23 5.5 16.5 4.5 8 C4.3 6.5 5.5 5 7 5 Z"/>
      </svg>
      9031 5582
    </li>
    <li class="contact-item">
      <svg class="contact-icon" viewBox="0 0 28 28" aria-hidden="true">
        <rect class="solid" x="8" y="6" width="12" height="19" rx="2"/>
        <rect x="10.5" y="9" width="7" height="5" fill="#fff" stroke="none"/>
        <path d="M11 3 L11 6"/>
      </svg>
      0417 3820194
    </li>
    <li class="contact-item">
      <svg class="contact-icon" viewBox="0 0 28 28" aria-hidden="true">
        <circle cx="14" cy="15" r="9"/>
        <path d="M5 15 H23 M14 6 C10 10 10 20 14 24 M14 6 C18 10 18 20 14 24"/>
      </svg>
      www.meko.com.au
    </li>
    <li class="contact-item">
      <svg class="contact-icon" viewBox="0 0 28 28" aria-hidden="true">
        <path d="M14 25 C9 19 6 15 6 11 A8 8 0 0 1 22 11 C22 15 19 19 14 25 Z" stroke-width="3"/>
        <circle cx="14" cy="11" r="3" stroke-width="2.6"/>
      </svg>
      12/86 Harbour street Kestrelton 3100
    </li>
    <li class="contact-item contact-indent">Kestrelton / Ashmere</li>
  </ul>
</main>
</body>
</html>
```